Lirra Dusk a young drag queen needs a website to promote herself

URLs: queenlirra.example / lirradusk.example
General Requests
• SEO-Optimized
• CMS: Joomla
Lirra Dusk is a young Drag queen still going to college and living in the us. She has an international Background with Canadian and Swiss citizenship. She is very creative not only in her Shows but she is also a painter, a Fashion designer a Music writer, a singer and an excellent vegan cook.

In order to promote her and to book her for a Show or a maquillage she needs a Website that will highly interact with social Media.

The Structure of the Website could be as follows:

Welcome page
From the Welcome page navigation to
1. Blog
a. Easy tool to add new Blogs
b. Possibility for others to write comments
c. Possibilty to
2. Events: Videos and Pictures
a. Easy Way to Ad Pictures and Vidoes and Showing a Title/Description
3. Upcoming Events and Shows
a. Possibility to describe Upcoming shows with link for more Information and Registration
4. Book a Show
a. I offer a lot of different Shows with Dancing, Singing or Moderating an Evening. Since I Speak English, (Swiss-)German and French I can entertain a multicultural Audience. Just get in touch with me and let’s discuss it.
b. Contact form for ordering an offer for a show (Name and Address; Kind of Show, Duration, Date, Place, Budget, Captcha)
c. lirra@lirradusk.example
5. Book a Maquillage
a. Do you want to look like a Drag? Are you a young Drag and want to learn how to get dressed up an a unique Maquillage? Do you want to have a special surprise for a Bachelors Party? Just ask me! I’m your Expert! Also available as Gift Certificate.
b. Contact form for ordering an offer for a Maquillage (Name and Address; Kind of Maquillage, Option for Gift Certificate; Occasion, Date, Place, Budget; captcha);
c. Form mailed to lirra@lirradusk.example
6. Lirra on Social Media
a. Join me on Facebook
b. Join me on Instagram
c. Join me on Soundcloud
7. Sponsors and Partners
a. Banner Glow Mesa
b. ….
Updates

Industry/Entity Type

College

Number of Pages Required

5+ page

Font styles to use
Decorative

Colors
6b449b
d2a4cc
e4daeb

Requirements
Must have
• Responsive Design

```html
<!DOCTYPE html>
<html lang="en">
<head>
<meta charset="utf-8">
<title>Lirra Dusk</title>
<link rel="stylesheet" href="https://fonts.googleapis.com/css2?family=Lato:wght@300;400;700&display=swap">
<style>
:root{
  --ink:#1b1b1b;
  --paper:#ffffff;
  --text-light:#ffffff;
  --text-muted:#8d8d8d;
  --text-dim:#6e6e6e;
  --nav-active:#9a9a9a;
  --button:#8a8a8a;
  --card-photo:#8c8c8c;
  --card-strip:#4d4d4d;
  --card-dark:#3b3b3b;
}
*{margin:0;padding:0;box-sizing:border-box}
html,body{width:833px;height:1200px;overflow:hidden;background:var(--paper)}
body{font-family:'Lato',sans-serif;color:var(--text-light)}
.page{position:relative;width:833px;height:1200px;overflow:hidden}
.backdrop{position:absolute;inset:0}
.abs{position:absolute}

.brand{left:0;width:833px;top:30px;text-align:center;font-size:34px;font-weight:300;letter-spacing:1px;color:var(--text-light)}
.social{top:42px;left:581px;display:flex;gap:8px}
.social span{width:24px;height:24px;border-radius:50%;background:var(--text-light);display:flex;align-items:center;justify-content:center}
.social span::after{content:"";width:18px;height:18px;border-radius:50%;border:1.5px solid var(--ink)}
.main-nav{top:103px;left:218px;display:flex;gap:25px;font-size:9px;font-weight:400;letter-spacing:.3px}
.main-nav a{color:var(--text-light);text-decoration:none}
.main-nav a.active{color:var(--nav-active)}

.hero-photo{left:0;top:0}
.dots{top:408px;left:394px;display:flex;gap:8px}
.dots span{width:8px;height:8px;border-radius:50%;border:1px solid #fff;display:block}
.dots span.on{background:#fff}

.welcome-title{left:163px;top:540px;font-size:20px;font-weight:700;line-height:1.15}
.welcome-title span{display:block;font-weight:300}
.welcome-text{left:163px;top:596px;width:250px;font-size:6.6px;line-height:1.5;color:var(--text-muted)}
.portrait{top:520px;width:82px;height:122px;background:
  radial-gradient(ellipse 60% 35% at 50% 30%,#f1eeef 0%,rgba(241,238,239,0) 70%),
  radial-gradient(ellipse 50% 30% at 50% 18%,#2c2a2b 0%,rgba(44,42,43,0) 80%),
  linear-gradient(180deg,#cfc9cc 0%,#b3adb0 45%,#3a3839 75%,#161616 100%)}

.event-title{left:163px;top:735px;font-size:22px;font-weight:700;color:var(--ink);line-height:1.15}
.event-title span{display:block;font-weight:300;color:var(--text-dim)}
.event-text{left:163px;top:792px;width:216px;font-size:6.4px;line-height:1.45;color:var(--text-muted)}
.event-button{left:204px;top:872px;width:125px;height:24px;background:var(--button);color:var(--text-light);font-size:9px;text-align:center;line-height:24px;letter-spacing:.3px}
.event-photo{left:422px;top:709px;width:248px;height:203px;background:
  radial-gradient(ellipse 35% 60% at 75% 70%,rgba(120,110,120,.55) 0%,rgba(120,110,120,0) 70%),
  linear-gradient(180deg,#7fb4c4 0%,#d9c9a4 22%,#f0c585 35%,#b98c6a 52%,#6f6a74 68%,#3d4150 100%)}
.arrow{top:808px;width:19px;height:19px}

.blog-title{left:0;width:833px;top:960px;text-align:center;font-size:20px;font-weight:700;line-height:1.1}
.blog-title span{display:block;font-weight:300}
.post{top:1021px;width:161px;height:108px}
.post-photo{background:var(--card-photo)}
.post-photo .strip{position:absolute;left:0;bottom:0;width:100%;height:24px;background:var(--card-strip);font-size:6.5px;font-weight:700;padding:9px 8px 0}
.post-dark{background:var(--card-dark);padding:12px 7px 0}
.post-dark h3{font-size:7px;font-weight:700;margin-bottom:6px}
.post-dark p{font-size:6px;line-height:1.5;color:#b5b5b5;margin-bottom:8px}
.post-dark .read{display:inline-block;background:#1e1e1e;font-size:5.5px;padding:4px 6px;margin-bottom:10px}
.post-dark .meta{font-size:5.5px;color:#b5b5b5}
</style>
</head>
<body>
<div class="page">
  <svg class="backdrop" width="833" height="1200" viewBox="0 0 833 1200" aria-hidden="true">
    <polygon points="0,0 833,0 833,132 0,120" fill="#1b1b1b"/>
    <polygon points="0,466 833,432 833,714 0,684" fill="#1b1b1b"/>
    <polygon points="0,938 833,894 833,1188 0,1200" fill="#1b1b1b"/>
  </svg>

  <svg class="abs hero-photo" width="833" height="470" viewBox="0 0 833 470" role="img" aria-label="Hero photo: performer in a golden gown posing against sandstone rocks">
    <defs>
      <linearGradient id="rockBase" x1="0" y1="0" x2="1" y2="1">
        <stop offset="0" stop-color="#5e452a"/>
        <stop offset="0.35" stop-color="#a8845a"/>
        <stop offset="0.65" stop-color="#c9a679"/>
        <stop offset="1" stop-color="#6f5538"/>
      </linearGradient>
      <radialGradient id="rockLight" cx="0.62" cy="0.45" r="0.45">
        <stop offset="0" stop-color="#dcc09a" stop-opacity="0.75"/>
        <stop offset="1" stop-color="#dcc09a" stop-opacity="0"/>
      </radialGradient>
      <radialGradient id="goldGlow" cx="0.5" cy="0.5" r="0.5">
        <stop offset="0" stop-color="#d9a43a" stop-opacity="0.85"/>
        <stop offset="1" stop-color="#d9a43a" stop-opacity="0"/>
      </radialGradient>
      <linearGradient id="rockShade" x1="0" y1="0" x2="0" y2="1">
        <stop offset="0" stop-color="#2e2115" stop-opacity="0.45"/>
        <stop offset="0.3" stop-color="#2e2115" stop-opacity="0"/>
        <stop offset="0.8" stop-color="#2e2115" stop-opacity="0"/>
        <stop offset="1" stop-color="#2e2115" stop-opacity="0.5"/>
      </linearGradient>
      <clipPath id="heroShape"><polygon points="0,168 833,132 833,408 0,466"/></clipPath>
    </defs>
    <g clip-path="url(#heroShape)">
      <rect width="833" height="470" fill="url(#rockBase)"/>
      <rect width="833" height="470" fill="url(#rockLight)"/>
      <ellipse cx="420" cy="330" rx="70" ry="140" fill="url(#goldGlow)"/>
      <rect width="833" height="470" fill="url(#rockShade)"/>
    </g>
  </svg>

  <div class="abs brand">Lirra Dusk</div>
  <div class="abs social" aria-label="Social links"><span></span><span></span><span></span></div>
  <nav class="abs main-nav">
    <a href="#">HOME</a><a class="active" href="#">BLOG</a><a href="#">EVENTS</a><a href="#">BOOK A SHOW</a><a href="#">BOOK A MAQUILLAGE</a><a href="#">CONTACT US</a>
  </nav>
  <div class="abs dots"><span class="on"></span><span class="on"></span><span></span></div>

  <h1 class="abs welcome-title">WELCOME<span>TO LIRRA DUSK WEBSITE!</span></h1>
  <p class="abs welcome-text">Lirra Dusk is a young Drag queen still going to college and living in the us. She has an international Background with Canadian and Swiss citizenship. She is very creative not only in her Shows but she is also a painter, a Fashion designer a Music writer, a singer and an excellent vegan cook.</p>
  <div class="abs portrait" style="left:420px" role="img" aria-label="Portrait photo of the performer in stage makeup and a black hat"></div>
  <div class="abs portrait" style="left:506px" role="img" aria-label="Portrait photo of the performer in stage makeup and a black hat"></div>
  <div class="abs portrait" style="left:592px" role="img" aria-label="Portrait photo of the performer in stage makeup and a black hat"></div>

  <h2 class="abs event-title">LAST EVENT<span>NEW YORK TOUR</span></h2>
  <p class="abs event-text">Lorem ipsum dolor sit amet, consectetur adipiscing elit. Interdum proin ligula tempor eros sodales parturient. Laoreet curae ridiculus consequat lectus mollis lacinia montes. Aenean commodo nostra elit imperdiet convallis pulvinar parturient taciti dui posuere conjectum. Class dignissim sed conubia ornare quae magna ipsum cum nullam ultrices curabitur eros. Litora duis velit tincidunt metus elit purus – lacus fermentum ipsum taciti.</p>
  <div class="abs event-button">SHOW MORE EVENTS</div>
  <div class="abs event-photo" role="img" aria-label="Event photo: city skyline with skyscrapers at sunset"></div>
  <svg class="abs arrow" style="left:130px" viewBox="0 0 19 19" aria-label="Previous"><circle cx="9.5" cy="9.5" r="9.5" fill="#111"/><polyline points="11,5.5 7,9.5 11,13.5" fill="none" stroke="#fff" stroke-width="2"/></svg>
  <svg class="abs arrow" style="left:682px" viewBox="0 0 19 19" aria-label="Next"><circle cx="9.5" cy="9.5" r="9.5" fill="#111"/><polyline points="8,5.5 12,9.5 8,13.5" fill="none" stroke="#fff" stroke-width="2"/></svg>

  <h2 class="abs blog-title">BLOG<span>LATEST POSTS</span></h2>
  <article class="abs post post-photo" style="left:163px" role="img" aria-label="Blog post image"><div class="strip">LOREM IPSUM DOLOR SIT AMET, CONLECER</div></article>
  <article class="abs post post-photo" style="left:336px" role="img" aria-label="Blog post image"><div class="strip">LOREM IPSUM DOLOR SIT AMET, CONLECER</div></article>
  <article class="abs post post-dark" style="left:510px">
    <h3>NULLA ERAT TORTOR, RHONCUS A DOLOR</h3>
    <p>Morbi semper viverra nibh vel finibus n hac habitasse platea dictumst. Donec eleifend eros id facilisis eras auctor, pellentesque et massa vel odio congue...</p>
    <span class="read">READ POST</span>
    <div class="meta">27 JULY &nbsp;|&nbsp; BY STEVIE IPSUM &nbsp;|&nbsp; 125 COMMENTS</div>
  </article>
</div>
</body>
</html>
```